Redesign of LinkwireSupply.com website

Revised description:
We would like to redesign our 8 year old website (in Wordpress) to something fresh and current. Although I've attached our log, we are open to a new logo if you have a cool idea but it should have linkwiresupply.com somewhere in the logo.  We are going to eventually put 5 rotating images on the homepage but for the interest of this design contest, I would like you to use  just one image (#23), only on the small laptop screen in the image, I would like to see the linkwiresupply homepage inserted (that you've designed) giving the illusion that whoever was using that laptop was looking at the linkwiresupply website. The tagline "your top-tier gear merits top-tier wiring." should be somewhere on the image as well.
This is an open slate, we are open to new colors, designs, etc. We really want something simple, not crowded with images, etc.
I have included a bunch of pictures to use or you can use your own. You can use the same product categories that we currently have on the website. There should also be a place on the homepage to insert our Youtube video.
We sell to businesses and get a lot of orders from the government and military so the site should be catered towards this market. We sell very little to consumers. Our biggest competitor is q7m.com but we don't really want something that looks like their site. Something closer to a zorva.com or kb.com is more what we're looking for. Please keep in mind that we also want people to know its a retail site, where they can purchase cables. The winner of this will likely have additional $$ work as we will be making a lot of product changes in the near future.

Target Market(s)
We sell fiber optic and copper cables to Government agencies, military, colleges/universities, small & large businesses. Mostly male. 25-50.
Industry/Entity Type
Government
Requirements
Must have
- We are different from our competition in the following ways:
1. FREE ground shipping on ALL orders
2. We build custom cables in the USA
3. We have a lifetime warranty on ALL of our cables so we use the highest quality components
4. We are on the west coast so we have up to 3 extra hours to ship our product for same day shipping
5. We stock over 100,000 different cables
6. Our prices are competitive
You can watch our Youtube video to get an idea : )
Nice to have
- I've included a lot of images below for inspiration or to use on the site when appropriate.
Here is a site that I really like. You need to cut and paste it.
http://layoutbazaar.example/item/pelora-site-theme-a-shop-theme/full_screen_preview/417093
Should not have
- Anything "cartoony" or whimsical.

```html
<!DOCTYPE html>
<html lang="en">
<head>
<meta charset="utf-8">
<title>LinkwireSupply.com – Home</title>
<link rel="stylesheet" href="https://fonts.googleapis.com/css2?family=Lato:ital,wght@0,400;0,700;1,400&display=swap">
<style>
:root{
  --navy:#1f3b6d;
  --navy-dark:#16294d;
  --black:#0d0a0d;
  --ink:#333;
  --muted:#8a8a8a;
  --rule:#c9ced8;
  --field:#dfe4ec;
  --paper:#ffffff;
  --band:#eeeeef;
}
*{box-sizing:border-box;margin:0;padding:0}
html,body{width:1200px;height:900px;overflow:hidden;background:var(--paper);font-family:'Lato',sans-serif;color:var(--ink)}
.abs{position:absolute}
.site-header{left:405px;top:0;width:392px;height:34px;background:var(--black)}
.brand{left:460px;top:7px;display:flex;align-items:center;gap:3px;color:#fff;font-size:8px;font-weight:700}
.brand-dot{width:7px;height:7px;border-radius:50%;background:var(--navy);border:1px solid #fff}
.brand-tag{left:528px;top:16px;font-size:3.5px;color:#bbb}
.main-nav{left:630px;top:14px;display:flex;gap:4px;font-size:4px;color:#ddd}
.main-nav span{padding:2px 3px}
.main-nav .is-active{background:#2a2f3a;border-radius:2px;color:#fff}
.search-label{left:646px;top:27px;font-size:4px;color:#fff;font-weight:700}
.search-field{left:681px;top:27px;width:53px;height:5px;background:var(--field);border-radius:3px}
.search-btn{left:737px;top:27px;width:8px;height:5px;background:var(--navy);border-radius:3px}
.info-bar{left:457px;top:36px;width:288px;height:14px;background:var(--band);font-size:3.5px;color:#555}
.info-bar span{position:absolute;top:5px}
.cart{left:650px;top:35px;width:85px;height:21px;background:var(--black);border-radius:3px}
.cart-icon{left:653px;top:37px;width:17px;height:17px;border-radius:50%;background:var(--navy)}
.cart-count{left:679px;top:39px;font-size:10px;color:#fff;font-weight:700}
.cart-meta{left:692px;top:40px;font-size:3.5px;color:#888;line-height:7px;text-align:right;width:38px}
.cart-meta b{color:#fff}
.hero{left:456px;top:52px;width:290px;height:144px;background:linear-gradient(#9aa6a4 0%,#6f7f72 22%,#8fb54a 45%,#a7cc4f 75%,#bcd867 100%)}
.hero-caption{left:500px;top:107px;width:202px;height:29px;background:rgba(30,30,30,.82);color:#fff;font-size:10.5px;text-align:center;line-height:13px;padding-top:2px}
.hero-arrow{width:8px;height:10px;background:var(--navy);top:117px;color:#fff;font-size:7px;text-align:center;line-height:10px}
.hero-dots{left:593px;top:173px;width:24px;height:6px;background:rgba(0,0,0,.5);border-radius:2px;display:flex;gap:2px;justify-content:center;align-items:center}
.hero-dots i{width:2.5px;height:2.5px;border-radius:50%;background:#fff;opacity:.7}
.tabs{display:flex;font-size:3.6px;font-weight:700}
.tabs span{width:48px;height:9px;line-height:9px;padding-left:4px;border:1px solid var(--navy);color:var(--navy)}
.tabs .is-active{background:var(--navy);color:#fff}
.see-all{left:697px;top:208px;font-size:3.5px;color:var(--muted)}
.product{width:78px}
.product-photo{height:62px}
.product-title{font-size:4.3px;font-style:italic;color:var(--navy);margin-top:9px}
.product-text{font-size:3.2px;color:var(--muted);line-height:5.5px;margin-top:3px}
.more{font-size:3.2px;color:var(--navy);text-align:right;margin-top:3px;font-weight:700}
.rule{height:2px;background:linear-gradient(90deg,transparent,var(--rule) 40%,var(--navy) 90%,var(--navy))}
.section-title{height:17px;text-align:center;font-size:9.5px;line-height:16px;letter-spacing:.3px}
.section-title.solid{background:var(--navy);color:#fff}
.section-title.outline{border:1px solid var(--navy);color:var(--navy)}
.video{left:458px;top:390px;width:108px;height:68px;background:linear-gradient(135deg,#1b4a9a,#3f80d0 55%,#16336b)}
.video-bar{left:458px;top:452px;width:108px;height:6px;background:#1c1c1c}
.about-text{left:575px;top:390px;width:158px;font-size:4.3px;line-height:5.5px;color:#777}
.about-text p{text-indent:8px}
.benefits{font-size:3.4px;color:#888;line-height:4.6px}
.benefits li{list-style:none;position:relative;padding-left:7px;margin-bottom:6px;width:75px}
.benefits li::before{content:"";position:absolute;left:0;top:1px;width:2px;height:2px;border-radius:50%;background:var(--navy)}
.quote{background:var(--navy);color:#fff;font-size:10px;text-align:center}
.quote-by{left:620px;top:620px;width:89px;text-align:right;font-size:3.2px;color:var(--muted)}
.quote-dots{left:601px;top:634px;display:flex;gap:2px;align-items:center}
.quote-dots i{width:5px;height:5px;border-radius:50%;border:1px solid var(--navy)}
.quote-dots i.dot{width:2.5px;height:2.5px;background:var(--navy)}
.cta{left:405px;top:682px;width:392px;text-align:center;font-size:8.5px;color:var(--navy)}
.contact-form{left:553px;top:716px;width:109px;height:116px;border:1px solid var(--navy)}
.form-head{height:15px;background:var(--navy);color:#fff;font-size:6px;text-align:center;line-height:15px}
.form-label{font-size:5.5px;color:var(--navy-dark);left:560px}
.form-field{left:600px;border:1px solid var(--navy);border-radius:3px;width:55px;height:11px}
.send{left:585px;top:819px;width:38px;height:8px;background:var(--navy);color:#fff;font-size:5px;text-align:center;line-height:8px}
.site-footer{left:405px;top:866px;width:392px;height:34px;background:var(--black);color:#fff;font-size:4.8px;text-align:center;line-height:34px}
</style>
</head>
<body>
<header>
  <div class="abs site-header"></div>
  <div class="abs brand"><span class="brand-dot"></span>linkwiresupply.com</div>
  <div class="abs brand-tag">Fiber Cables at Your Fingertips</div>
  <nav class="abs main-nav"><span class="is-active">Home</span><span>The store</span><span>Our news</span><span>FAQ</span><span>Contact us</span></nav>
  <div class="abs search-label">Search products:</div>
  <div class="abs search-field"></div>
  <div class="abs search-btn"></div>
  <div class="abs info-bar"><span style="left:10px">linkwiresupply.com</span><span style="left:66px">✆ 555-014-2237</span></div>
  <div class="abs cart"></div>
  <div class="abs cart-icon"><svg width="17" height="17" viewBox="0 0 17 17"><path d="M4 5h2l1.5 5h5l1-3.5H7" fill="none" stroke="#fff" stroke-width="1"/><circle cx="8" cy="12" r=".9" fill="#fff"/><circle cx="12" cy="12" r=".9" fill="#fff"/></svg></div>
  <div class="abs cart-count">0</div>
  <div class="abs cart-meta">products in basket<br>Total: <b>$0.00</b></div>
</header>

<section>
  <div class="abs hero" role="img" aria-label="Two coiled fiber patch cables over a green field with hills behind"></div>
  <div class="abs hero-caption">Your top-tier gear merits top-tier<br>wiring</div>
  <div class="abs hero-arrow" style="left:456px">‹</div>
  <div class="abs hero-arrow" style="left:739px">›</div>
  <div class="abs hero-dots"><i></i><i></i><i></i><i></i></div>
</section>

<section>
  <div class="abs tabs" style="left:472px;top:205px"><span class="is-active">NEW PRODUCTS</span><span>BESTSELLERS</span></div>
  <div class="abs see-all">see all of our cables ›</div>
  <article class="abs product" style="left:471px;top:222px">
    <div class="product-photo" role="img" aria-label="Orange and yellow patch cable with ST and LC connectors" style="background:linear-gradient(135deg,#fff,#f3c9a4 40%,#f2e27a 70%,#fff)"></div>
    <h3 class="product-title">Mode Conditioning Patch Cable</h3>
    <p class="product-text">Combines singlemode and multimode fiber with a controlled launch offset. Cable is made from premium optical fiber with ceramic LC &amp; ST connectors. Each cable is individually bagged with test results.</p>
    <p class="more">more info »</p>
  </article>
  <article class="abs product" style="left:560px;top:222px">
    <div class="product-photo" role="img" aria-label="Coiled aqua twelve-fiber breakout cable in a clear tray" style="background:radial-gradient(ellipse at center,#bfe7ee,#8fd2df 55%,#e6eef2)"></div>
    <h3 class="product-title">12 Fiber 50/125 OM3, 10 GIG LC</h3>
    <p class="product-text">Each fiber breakout is tied to its own color-coded buffer for easy identification and the cable jacket is clearly marked. Connectors are ceramic with a PC polish. Each cable ships with test results and a lifetime guarantee.</p>
    <p class="more">more info »</p>
  </article>
  <article class="abs product" style="left:647px;top:222px">
    <div class="product-photo" role="img" aria-label="Blue duplex fiber cable with beige LC connectors" style="background:linear-gradient(160deg,#fff,#5b6fd6 35%,#d9d3c0 60%,#fff)"></div>
    <h3 class="product-title">Multimode Duplex 62.5/125 LC LC -</h3>
    <p class="product-text">Multimode duplex 62.5/125 riser-rated cable with ceramic LC connectors on both ends. The fiber jacket is blue and each cable is individually bagged with test results. Please allow up to 3 days to ship.</p>
    <p class="more">more info »</p>
  </article>
  <div class="abs rule" style="left:472px;top:344px;width:260px"></div>
</section>

<section>
  <h2 class="abs section-title solid" style="left:549px;top:357px;width:101px">ABOUT US</h2>
  <div class="abs video" role="img" aria-label="Company video still with a customer service team"></div>
  <div class="abs video-bar"></div>
  <div class="abs about-text">
    <p>LinkwireSupply's team of industry professionals has a combined 20 years of experience in all areas of the cable and connectivity business. The company was created to give customers a convenient place to shop on-line for products to meet their connectivity needs.</p>
    <p>Due to our extensive inventory we can ship many products on a same day/next day basis. We also have quick turn around time on custom cable assemblies.</p>
    <p>We purchase raw material directly from the fiber cable manufacturer so you save on distribution cost. There is no middle man between you and LinkwireSupply.</p>
  </div>
</section>

<section>
  <h2 class="abs section-title outline" style="left:545px;top:473px;width:113px">OUR BENEFITS</h2>
  <ul class="abs benefits" style="left:475px;top:503px"><li>FREE GROUND SHIPPING ON ALL ORDERS</li><li>WE HAVE A LIFETIME WARRANTY ON ALL OF OUR CABLES SO WE USE THE HIGHEST QUALITY COMPONENTS</li></ul>
  <ul class="abs benefits" style="left:563px;top:503px"><li>WE BUILD CUSTOM CABLES IN THE USA</li><li>WE STOCK OVER 100,000 DIFFERENT CABLES</li></ul>
  <ul class="abs benefits" style="left:652px;top:503px"><li>OUR PRICES ARE COMPETITIVE</li><li>WE ARE ON THE WEST COAST SO WE HAVE UP TO 3 EXTRA HOURS TO SHIP OUR PRODUCT FOR SAME DAY SHIPPING</li></ul>
  <div class="abs rule" style="left:472px;top:543px;width:260px"></div>
</section>

<section>
  <div class="abs tabs" style="left:472px;top:552px"><span class="is-active">FEEDBACK</span><span>OUR CLIENTS</span></div>
  <div class="abs quote" style="left:508px;top:584px;width:201px;height:19px;line-height:19px">Best quality fibre cables I've ever used.</div>
  <div class="abs quote" style="left:537px;top:600px;width:143px;height:16px;line-height:12px">You are professionals.</div>
  <div class="abs quote-by">Jon Name, Sample Company</div>
  <div class="abs quote-dots"><i></i><i class="dot"></i><i></i></div>
  <div class="abs rule" style="left:472px;top:651px;width:260px"></div>
</section>

<section>
  <h2 class="abs cta">WE'RE READY TO ANSWER YOUR QUESTIONS</h2>
  <form class="abs contact-form"><div class="form-head">CONTACT FORM</div></form>
  <label class="abs form-label" style="top:741px">Your name</label>
  <div class="abs form-field" style="top:739px"></div>
  <label class="abs form-label" style="top:757px">Your email</label>
  <div class="abs form-field" style="top:755px"></div>
  <label class="abs form-label" style="top:782px">Your question</label>
  <div class="abs form-field" style="top:774px;width:59px;height:26px"></div>
  <div class="abs send">SEND</div>
</section>

<footer class="abs site-footer">PH (555) 014-2237 · FAX: (555) 014-8890 – 48 Calle Ventana, Mission Hollow, CA 90010</footer>
</body>
</html>
```